Sci-Fi themed EP cover needed for Wrenlox/oVardo

Need a cover for a 3 track EP for Wrenlox and other streaming services. The artist name is 'HollowMarbleHarbor', logo design is attached. Would also like a slightly animated version to use as an Brellowin story. Ideas for design: Movie poster feel, extreme weather, large industrial building, corrosion/rust, dark industrial robot, futuristic.

```html
<!DOCTYPE html>
<html lang="en">
<head>
<meta charset="utf-8">
<title>HollowMarbleHarbor – 3 Track EP</title>
<link rel="stylesheet" href="https://fonts.googleapis.com/css2?family=Black+Ops+One&display=swap">
<style>
  :root {
    --page-bg: #e9e9e9;
    --cover-deep: #0a0c55;
    --cover-mid: #101476;
    --cover-violet: #4a1fb8;
    --cover-blue: #1f5be0;
    --neon: #5ff3ff;
    --title: #c6f7ff;
    --subtitle: #3fe6f5;
  }
  * { margin: 0; padding: 0; box-sizing: border-box; }
  html, body {
    width: 1200px;
    height: 960px;
    overflow: hidden;
    background: var(--page-bg);
  }
  .canvas {
    position: relative;
    width: 1200px;
    height: 960px;
    display: flex;
    align-items: center;
    justify-content: center;
  }
  .ep-cover {
    position: relative;
    width: 860px;
    height: 860px;
    background: radial-gradient(ellipse at 55% 40%, var(--cover-mid) 0%, var(--cover-deep) 70%);
    overflow: hidden;
  }
  .circuit-art {
    position: absolute;
    inset: 0;
    background:
      radial-gradient(ellipse 45% 55% at 0% 20%, rgba(120, 60, 230, 0.55) 0%, transparent 70%),
      radial-gradient(ellipse 50% 60% at 100% 85%, rgba(40, 110, 240, 0.6) 0%, transparent 70%),
      radial-gradient(ellipse 30% 25% at 90% 8%, rgba(40, 110, 240, 0.35) 0%, transparent 70%),
      radial-gradient(ellipse 30% 20% at 8% 95%, rgba(40, 110, 240, 0.3) 0%, transparent 70%);
  }
  .neon-frame {
    position: absolute;
    inset: 22px;
    border: 3px solid var(--neon);
    box-shadow: 0 0 10px var(--neon), inset 0 0 10px rgba(95, 243, 255, 0.6);
  }
  .artist-name {
    position: absolute;
    left: 0;
    right: 0;
    top: 255px;
    text-align: center;
    font-family: "Black Ops One", sans-serif;
    font-weight: 400;
    color: var(--title);
    line-height: 1;
  }
  .artist-name__top {
    display: block;
    font-size: 150px;
    letter-spacing: 2px;
  }
  .artist-name__bottom {
    display: block;
    margin-top: 10px;
    font-size: 62px;
    letter-spacing: 1px;
  }
  .release-type {
    position: absolute;
    left: 0;
    right: 0;
    top: 542px;
    text-align: center;
    font-family: "Black Ops One", sans-serif;
    font-size: 24px;
    letter-spacing: 6px;
    color: var(--subtitle);
  }
</style>
</head>
<body>
  <main class="canvas">
    <section class="ep-cover">
      <div class="circuit-art" role="img" aria-label="Glowing blue and violet circuit-board traces in the cover corners"></div>
      <div class="neon-frame"></div>
      <h1 class="artist-name">
        <span class="artist-name__top">HOLLOW</span>
        <span class="artist-name__bottom">MARBLEHARBOR</span>
      </h1>
      <p class="release-type">3 TRACK EP</p>
    </section>
  </main>
</body>
</html>
```